Edgy rebranded biz cards QBL

We are rebranding our 20 yr old mortgage company with a new logo and would like cards to compliment our new look.

Target Market(s)

potential home buyers or clients for refinance

Industry/Entity Type

Mortgage Brokerage

Contact Information for Business Card

418 W. Tamsin Rd #340
Henderson, NV 89152
702.481.5927 o
702-481-5920 f
www.quarrybluelend,com
nmls 612084
QBL is an equal housing lender

Font styles to use
Sans Serif

Colors
0455a3
3176b5
0393ce
33a6d7

Requirements
Must have
• space for a photo
Nice to have
• One side with the company info and the other with the person's info

```html
<!DOCTYPE html>
<html lang="en">
<head>
<meta charset="utf-8">
<title>Quarry Blue Lending – Business Card</title>
<link rel="stylesheet" href="https://fonts.googleapis.com/css2?family=Montserrat:wght@400;600;700&display=swap">
<style>
  :root {
    --brand-blue: #1177bf;
    --deep-blue: #0455a3;
    --ink-blue: #1a6fb8;
    --text-gray: #4a4a4a;
    --soft-gray: #8c8c8c;
    --photo-gray: #9a9a9a;
    --tab-gray: #8a8a8a;
    --card-white: #ffffff;
    --backdrop: #e9e9e9;
  }
  * { margin: 0; padding: 0; box-sizing: border-box; }
  html, body { width: 963px; height: 1200px; overflow: hidden; }
  body {
    position: relative;
    background: var(--backdrop);
    font-family: "Montserrat", sans-serif;
  }
  .card {
    position: absolute;
    left: 194px;
    width: 576px;
    height: 330px;
    overflow: hidden;
  }
  .card--front { top: 214px; background: var(--card-white); }
  .card--back { top: 627px; background: var(--brand-blue); }

  .brand-mark {
    position: absolute;
    display: flex;
    align-items: center;
    gap: 8px;
    font-weight: 700;
    letter-spacing: 0.5px;
    white-space: nowrap;
  }
  .brand-mark__square { display: block; }
  .card--front .brand-mark {
    left: 38px; top: 58px;
    font-size: 17px;
    color: var(--ink-blue);
  }
  .card--front .brand-mark__square { width: 14px; height: 14px; background: var(--ink-blue); }

  .edge-tabs { position: absolute; left: 0; top: 138px; }
  .edge-tabs span { display: block; width: 8px; height: 18px; background: var(--tab-gray); margin-bottom: 3px; }

  .person { position: absolute; left: 38px; top: 140px; }
  .person__name { font-size: 18px; font-weight: 700; color: var(--ink-blue); letter-spacing: 1px; }
  .person__title { font-size: 13px; color: var(--soft-gray); margin-top: 2px; }

  .details { position: absolute; left: 38px; top: 186px; font-size: 13px; color: var(--text-gray); line-height: 16px; }
  .details__nmls { margin-top: 9px; margin-left: 2px; }
  .contact-list { list-style: none; margin-top: 6px; }
  .contact-list li { display: flex; align-items: center; gap: 6px; height: 16.5px; }
  .contact-list svg { width: 11px; height: 11px; flex: none; }

  .photo-space {
    position: absolute;
    left: 312px; top: 24px;
    width: 264px; height: 292px;
    background: linear-gradient(180deg, #a3a3a3 0%, var(--photo-gray) 100%);
    border-radius: 120px 0 0 0;
  }

  .footer-band { position: absolute; left: 0; bottom: 0; width: 100%; height: 12px; background: var(--brand-blue); }

  .card--back .brand-mark {
    left: 0; right: 0; top: 138px;
    justify-content: center;
    font-size: 28px;
    color: #3fd4f2;
  }
  .card--back .brand-mark__square { width: 22px; height: 22px; background: #3fd4f2; }
  .lender-note {
    position: absolute; left: 0; right: 0; top: 288px;
    text-align: center;
    font-size: 13px;
    color: var(--card-white);
    letter-spacing: 0.3px;
  }
</style>
</head>
<body>
  <section class="card card--front">
    <div class="brand-mark"><span class="brand-mark__square"></span>QUARRY BLUE LENDING</div>
    <div class="edge-tabs"><span></span><span></span></div>
    <div class="person">
      <h1 class="person__name">DANIEL REYES</h1>
      <p class="person__title">President</p>
    </div>
    <div class="details">
      <p>418 W. Tamsin Rd #340<br>Henderson, NV 89152</p>
      <p class="details__nmls">NMLS : 612084</p>
      <ul class="contact-list">
        <li><svg viewBox="0 0 24 24"><path fill="#1a6fb8" d="M6.6 10.8a15 15 0 0 0 6.6 6.6l2.2-2.2c.3-.3.7-.4 1-.2 1.1.4 2.3.6 3.6.6.6 0 1 .4 1 1V20c0 .6-.4 1-1 1A17 17 0 0 1 3 4c0-.6.4-1 1-1h3.5c.6 0 1 .4 1 1 0 1.3.2 2.5.6 3.6.1.3 0 .7-.2 1z"/></svg>702.481.5927</li>
        <li><svg viewBox="0 0 24 24"><rect x="6" y="2" width="12" height="20" rx="2" fill="none" stroke="#1a6fb8" stroke-width="2.5"/></svg>702-481-5920</li>
        <li><svg viewBox="0 0 24 24"><circle cx="12" cy="12" r="10" fill="#1a6fb8"/><path d="M2 12h20M12 2c3 3 3 17 0 20M12 2c-3 3-3 17 0 20" stroke="#fff" stroke-width="1.5" fill="none"/></svg>www.quarrybluelend.com</li>
      </ul>
    </div>
    <div class="photo-space" role="img" aria-label="Space for a portrait photo of the team member"></div>
    <div class="footer-band"></div>
  </section>

  <section class="card card--back">
    <div class="brand-mark"><span class="brand-mark__square"></span>QUARRY BLUE LENDING</div>
    <p class="lender-note">QBL is an Equal Housing Lender</p>
  </section>
</body>
</html>
```